FC Varnet - Powerpoint for Sponsorship proposal

1. Introduction:
FC Varnet is seeking the development of a professional PowerPoint template to be used for club presentations, including the annual general meeting and sponsorship proposals. This template should reflect our club's identity, values, and colors, ideally incorporating the club's jersey colors.

2. Design Elements:

Color Scheme: The template should prominently feature FC Varnet's primary colors, which are red and blue, to create a strong visual association with the club.

Logo Integration: Include the club's logo in a tasteful and visible manner on each slide. The logo should be placed in a way that doesn't distract from the content but reinforces the club's identity.

Jersey Colors: If possible, incorporate the colors of the club's jerseys into the design elements or backgrounds to create a cohesive look.

3. Slide Layouts:
The template should include various slide layouts to accommodate the different sections of the presentations. Specific slide layouts should be designed for the following sections:

Title Slide: An impressive title slide with the club's logo, name, and potentially an image representing the club.

Objectives and Values: A clean and organized layout for presenting the club's objectives and core values.

Member Summary: A section for summarizing club members, categorized by type (e.g., players, coaches, volunteers).

Nationalities: A section for displaying a summary of the nationalities represented in the club.

Rankings Table: A visually appealing format for displaying league standings or rankings.

Committee Members: A slide template for introducing committee members, including their names, roles, and photos.

Financial Report: A structured layout for presenting financial data, including balance sheets and profit and loss statements.

Sponsorship Opportunities: A section for outlining the various sponsorship opportunities available, with clear details and benefits for potential sponsors.

4. Typography and Consistency:
Ensure that typography is consistent throughout the template, using easily readable fonts. Define font styles for headings, subheadings, and body text to maintain a professional look.

5. Imagery:
Incorporate high-quality images, such as action shots of matches or club events, to enhance the visual appeal of the template.

6. Simplicity and Clarity:
Maintain a clean, uncluttered design that prioritizes clarity and easy comprehension of the content. Avoid overly complex graphics or animations.

7. Customizability:
The template should be easily customizable, allowing presenters to add their content while preserving the overall design and branding.

8. Deliverables:
Provide the PowerPoint template in a format compatible with Microsoft PowerPoint.

Presentation to members or potential sponsors

Football

Sans Serif

0054AA
0677BA
7BADD7
CADEEF
E8F1F8
0094D4
00A9DD
6FCCEA
C7EBF8
E9F6FB
EB3D1F
EC4F4E
F09395
F8D3D4
FCEDEE

• See Project desscription

```html
<!DOCTYPE html>
<html lang="fr">
<head>
<meta charset="utf-8">
<title>FC Varnet – Dossier sponsoring 2024</title>
<link rel="stylesheet" href="https://fonts.googleapis.com/css2?family=Oswald:wght@500;700&family=Roboto:wght@400;500;700;900&display=swap">
<style>
  :root {
    --blue-deep: #0054AA;
    --blue-mid: #0677BA;
    --blue-bright: #0094D4;
    --blue-sky: #00A9DD;
    --blue-light: #6FCCEA;
    --blue-pale: #C7EBF8;
    --red: #EB3D1F;
    --red-soft: #EC4F4E;
    --red-pale: #F09395;
    --ink: #111111;
    --paper: #F4F5F7;
    --stage: #E2E3E6;
    --white: #FFFFFF;
  }
  * { box-sizing: border-box; margin: 0; padding: 0; }
  html, body { width: 729px; height: 1200px; overflow: hidden; }
  body { background: var(--stage); font-family: "Roboto", sans-serif; color: var(--ink); position: relative; }

  .page { position: absolute; overflow: hidden; }
  .ground { position: absolute; left: 0; right: 0; bottom: 0; background: var(--ink); }
  .placeholder { position: absolute; }

  /* Cover */
  .cover { left: 64px; top: 40px; width: 600px; height: 400px;
    background: radial-gradient(circle at 72% 40%, #EAF7FD 0%, var(--blue-light) 30%, var(--blue-sky) 60%, var(--blue-bright) 100%); }
  .cover .ground { height: 70px; }
  .club-mark { position: absolute; left: 34px; top: 30px; display: flex; align-items: center; gap: 8px;
    font-weight: 700; font-size: 18px; color: var(--white); }
  .club-mark .dot { width: 22px; height: 22px; border-radius: 50%; background: var(--red); }
  .cover-title { position: absolute; left: 34px; top: 100px; font-family: "Oswald", sans-serif; font-weight: 700;
    font-size: 52px; line-height: 1.02; color: var(--white); text-transform: uppercase; }
  .cover-art { right: 30px; top: 30px; width: 280px; height: 300px; border-radius: 140px 140px 0 0;
    background: linear-gradient(180deg, var(--red-soft) 0%, var(--red) 60%, #1b1b1b 100%); opacity: .85; }
  .cover-date { position: absolute; right: 28px; bottom: 24px; font-family: "Oswald", sans-serif; font-weight: 500;
    font-size: 17px; color: var(--white); }
  .cover-web { position: absolute; left: 34px; bottom: 24px; display: flex; align-items: center; gap: 7px;
    font-size: 15px; letter-spacing: 1px; color: var(--white); }
  .cover-web .globe { width: 12px; height: 12px; border-radius: 50%; background: var(--blue-sky); }

  /* Spreads */
  .spread { position: absolute; left: 24px; width: 680px; height: 250px; display: flex; box-shadow: 0 6px 14px rgba(0,0,0,.12); }
  .spread .page { position: relative; width: 340px; height: 250px; }
  .spread-club { top: 490px; }
  .spread-season { top: 810px; }

  .page-section { background: linear-gradient(160deg, var(--blue-light) 0%, var(--blue-sky) 45%, var(--blue-bright) 100%); }
  .page-section .ground { height: 44px; }
  .section-art { left: 26px; top: 70px; width: 70px; height: 150px; border-radius: 32px 32px 6px 6px;
    background: linear-gradient(180deg, #E3B21C 0%, #E3B21C 35%, var(--ink) 36%, var(--ink) 100%); }
  .section-title { position: absolute; left: 110px; top: 80px; font-size: 24px; font-weight: 500; color: var(--ink);
    line-height: 1.1; white-space: nowrap; }
  .section-tag { position: absolute; left: 112px; top: 114px; background: var(--ink); color: var(--white);
    font-size: 9px; padding: 3px 9px; border-radius: 10px; white-space: nowrap; }

  .page-light { background: var(--paper); }
  .page-light .ground { height: 30px; }
  .page-heading { position: absolute; left: 22px; top: 18px; font-size: 19px; font-weight: 500; color: var(--blue-mid); }

  .objective { position: absolute; left: 16px; width: 180px; }
  .objective .num { position: absolute; right: -26px; top: -2px; width: 20px; height: 20px; border-radius: 50%;
    color: var(--white); font-size: 9px; font-weight: 700; display: flex; align-items: center; justify-content: center; }
  .objective h3 { font-size: 10.5px; font-weight: 500; margin-bottom: 3px; text-align: right; white-space: nowrap; }
  .objective p { font-size: 7px; line-height: 1.35; color: #555; text-align: right; }
  .obj-blue h3 { color: var(--blue-mid); } .obj-blue .num { background: var(--blue-mid); }
  .obj-red h3 { color: var(--red); } .obj-red .num { background: var(--red); }
  .obj-dark h3 { color: var(--ink); } .obj-dark .num { background: var(--ink); }
  .objective-chart { position: absolute; right: 10px; top: 60px; }

  .season-title { position: absolute; left: 22px; top: 16px; font-size: 19px; font-weight: 500; color: var(--blue-deep); }
  .stat-board { position: absolute; left: 0; top: 48px; }
  .stat-board text { font-family: "Roboto", sans-serif; fill: var(--white); }
  .page-season .ground { height: 22px; }

  .map-art { left: 30px; top: 54px; width: 280px; height: 150px; border-radius: 50%;
    background: radial-gradient(ellipse, #DADDE2 0%, #E8EAED 60%, var(--paper) 100%); }
  .nation-chart { position: absolute; left: 0; top: 0; }
  .nation-chart text { font-family: "Roboto", sans-serif; }
  .nation-total { position: absolute; left: 150px; top: 196px; font-size: 17px; font-weight: 700; color: var(--red); }
  .runner-art { right: 18px; top: 178px; width: 24px; height: 44px; border-radius: 12px 12px 4px 4px; background: var(--ink); }
  .runner-art-left { left: 14px; top: 192px; width: 30px; height: 30px; border-radius: 14px 14px 4px 4px; background: var(--ink); }
</style>
</head>
<body>

<section class="page cover">
  <div class="placeholder cover-art" role="img" aria-label="Illustration: joueur en silhouette faisant un retourné devant une arche rouge, ballon éclaboussé"></div>
  <div class="club-mark"><span class="dot"></span>FC Varnet</div>
  <h1 class="cover-title">Dossier<br>sponsoring<br>2024</h1>
  <div class="ground"></div>
  <div class="cover-web"><span class="globe"></span>www.fcvarnet.com</div>
  <div class="cover-date">FC VARNET – 26 AOÛT 2021</div>
</section>

<section class="spread spread-club">
  <div class="page page-section">
    <div class="placeholder section-art" role="img" aria-label="Illustration: joueur en maillot jaune, mains sur les hanches, pied sur le ballon"></div>
    <h2 class="section-title">Le club en général</h2>
    <span class="section-tag">Objectifs, manifestations, événements</span>
    <div class="ground"></div>
  </div>
  <div class="page page-light">
    <h2 class="page-heading">Nos objectifs et motivations</h2>
    <div class="objective obj-blue" style="top:56px">
      <span class="num">01</span>
      <h3>Le football pour tous</h3>
      <p>Rendre le football accessible à chaque enfant de la région.</p>
    </div>
    <div class="objective obj-red" style="top:112px">
      <span class="num">02</span>
      <h3>Le football pour progresser</h3>
      <p>Former des joueurs et des éducateurs de qualité.</p>
    </div>
    <div class="objective obj-dark" style="top:162px">
      <span class="num">03</span>
      <h3>Le football comme facteur d'identité</h3>
      <p>Faire du stade un lieu de rencontre pour tous.</p>
    </div>
    <svg class="objective-chart" width="96" height="106" viewBox="0 0 100 110">
      <g transform="translate(50 55) rotate(-90)" fill="none" stroke-width="24">
        <circle r="36" stroke="var(--blue-bright)" stroke-dasharray="72 154"/>
        <circle r="36" stroke="var(--red)" stroke-dasharray="72 154" stroke-dashoffset="-77"/>
        <circle r="36" stroke="var(--ink)" stroke-dasharray="70 156" stroke-dashoffset="-154"/>
      </g>
    </svg>
    <div class="ground"></div>
  </div>
</section>

<section class="spread spread-season">
  <div class="page page-light page-season">
    <h2 class="season-title">FC Varnet saison 2021/22</h2>
    <svg class="stat-board" width="340" height="180" viewBox="0 0 340 180">
      <polygon points="0,8 180,8 196,30 180,52 0,52" fill="var(--blue-mid)"/>
      <polygon points="0,58 180,58 196,80 180,102 0,102" fill="var(--blue-deep)"/>
      <polygon points="0,108 180,108 196,130 180,152 0,152" fill="var(--red)"/>
      <polygon points="192,4 340,4 340,56 192,56 208,30" fill="var(--red)"/>
      <polygon points="192,60 340,60 340,112 192,112 208,86" fill="var(--blue-mid)"/>
      <text x="14" y="27" font-size="12" font-weight="700">598 membres actifs (+ 11.8 %)</text>
      <text x="14" y="38" font-size="6">NON COMPRIS LES 24 FILLES DE MORVEL</text>
      <text x="14" y="46" font-size="6">JOUANT POUR LE GROUPEMENT</text>
      <text x="14" y="85" font-size="12" font-weight="700">dont 92 filles (21.5 %)</text>
      <text x="14" y="131" font-size="12" font-weight="700">dont 92 dans encadrement</text>
      <text x="14" y="143" font-size="6">ENTRAÎNEURS, COACHS, COMITÉ, CANTINIERS</text>
      <text x="222" y="34" font-size="12" font-weight="700">76.4% de junior</text>
      <text x="222" y="90" font-size="12" font-weight="700">26 équipes (+1)</text>
    </svg>
    <div class="ground"></div>
  </div>
  <div class="page page-light">
    <h2 class="page-heading">Le football, facteur d'intégration</h2>
    <div class="placeholder map-art" role="img" aria-label="Carte du monde en gris clair"></div>
    <svg class="nation-chart" width="340" height="250" viewBox="0 0 340 250">
      <g transform="translate(170 120)">
        <path d="M0,0 L0,-40 A40,40 0 1 1 -27.4,29.2 Z" fill="var(--red)"/>
        <path d="M0,0 L-27.4,29.2 A40,40 0 0 1 -32.4,-23.5 Z" fill="#1E8A3E"/>
        <path d="M0,0 L-32.4,-23.5 A40,40 0 0 1 -12.4,-38 Z" fill="var(--blue-deep)"/>
        <path d="M0,0 L-12.4,-38 A40,40 0 0 1 0,-40 Z" fill="var(--red-pale)"/>
      </g>
      <g stroke="#888" stroke-width="0.7" fill="none">
        <polyline points="190,100 230,60 270,60"/>
        <polyline points="150,90 130,78 80,78"/>
        <polyline points="140,115 80,118"/>
        <polyline points="150,148 130,168 80,168"/>
      </g>
      <g font-size="8" font-weight="700" fill="var(--white)" text-anchor="middle">
        <circle cx="262" cy="60" r="10" fill="var(--red)"/><text x="262" y="63">62%</text>
        <circle cx="88" cy="78" r="10" fill="var(--red)"/><text x="88" y="81">10%</text>
        <circle cx="88" cy="118" r="10" fill="var(--red)"/><text x="88" y="121">5%</text>
        <circle cx="88" cy="168" r="10" fill="var(--red)"/><text x="88" y="171">23%</text>
      </g>
      <g font-size="10" font-weight="500" fill="var(--ink)">
        <text x="276" y="63">Suisse</text>
        <text x="36" y="81">France</text>
        <text x="36" y="121">Autres</text>
        <text x="26" y="171">Portugal</text>
      </g>
    </svg>
    <div class="nation-total">26 nationalités</div>
    <div class="placeholder runner-art" role="img" aria-label="Silhouette d'un joueur en course"></div>
    <div class="placeholder runner-art-left" role="img" aria-label="Silhouettes de joueurs se disputant le ballon"></div>
    <div class="ground"></div>
  </div>
</section>

</body>
</html>
```